Painting services company needs a DL brochure about their services

We need a brochure describing our painting services including our logo and photos of work. The final design needs to be colourful, vibrant, and targeted to schools, aged care, commercial property maintenance clients.

```html
<!DOCTYPE html>
<html lang="en">
<head>
<meta charset="utf-8">
<title>Brightcoat Painters – DL Brochure</title>
<link href="https://fonts.googleapis.com/css2?family=Oswald:wght@300;400;500;600&family=Lato:wght@400;700&display=swap" rel="stylesheet">
<style>
  :root {
    --navy: #16408a;
    --navy-deep: #0f2f6b;
    --gold: #e8ab17;
    --paper: #efeee9;
    --white: #ffffff;
    --ink: #2b2b2b;
    --stage: #c98c10;
  }
  * { box-sizing: border-box; margin: 0; padding: 0; }
  html, body { width: 1200px; height: 857px; overflow: hidden; }
  body { background: var(--stage); font-family: "Lato", sans-serif; color: var(--ink); }

  .brochure {
    position: absolute; top: 46px; width: 360px; height: 764px;
    background: var(--paper); overflow: hidden;
    box-shadow: 0 10px 30px rgba(0,0,0,.25);
  }
  .brochure--front { left: 200px; }
  .brochure--back { left: 640px; }

  .block { position: absolute; }
  .photo { position: absolute; }
  .heading { font-family: "Oswald", sans-serif; text-transform: uppercase; line-height: 1.05; }

  /* front */
  .front__topline { left: 0; top: 0; width: 100%; height: 6px; background: var(--navy); }
  .front__hero { left: 0; top: 6px; width: 100%; height: 330px;
    background: linear-gradient(180deg,#c9ccd1 0%,#8c8f94 50%,#55575c 100%); }
  .brand { left: 105px; top: 26px; width: 150px; height: 128px; background: var(--white);
    box-shadow: 0 3px 8px rgba(0,0,0,.3); display: flex; flex-direction: column;
    align-items: center; justify-content: center; gap: 8px; }
  .brand__mark { width: 22px; height: 22px; background: var(--gold); }
  .brand__name { font-family: "Oswald", sans-serif; font-weight: 600; color: var(--navy);
    font-size: 20px; line-height: 1.05; text-align: center; text-transform: lowercase; }

  .intro { left: 0; top: 336px; width: 100%; height: 190px; }
  .intro__grey { left: 0; top: 0; width: 46%; height: 100%; background: var(--paper); }
  .intro__gold { left: 46%; top: 0; width: 54%; height: 100%; background: var(--gold);
    padding: 24px 18px 0 30px; color: var(--white); font-size: 23px; }
  .intro__gold::before { content: ""; position: absolute; left: -12px; top: 68px;
    border-top: 12px solid transparent; border-bottom: 12px solid transparent;
    border-right: 12px solid var(--gold); }
  .intro__gold .light { font-weight: 300; }
  .intro__gold .strong { font-weight: 500; }
  .intro__gold .navy { font-weight: 500; color: var(--navy-deep); }

  .front__corridor { left: 0; top: 526px; width: 46%; height: 238px;
    background: linear-gradient(160deg,#e6e3da 0%,#b7ad96 55%,#7a7462 100%); }
  .tagline { left: 38px; top: 372px; width: 128px; height: 178px; background: var(--paper);
    border: 4px solid var(--navy); padding: 14px 10px; z-index: 2; }
  .tagline__title { color: var(--navy); font-weight: 600; font-size: 15px; }
  .tagline__sub { color: #444; font-weight: 300; font-size: 13px; margin-top: 12px; line-height: 1.5; }

  .specialist { left: 46%; top: 526px; width: 54%; height: 238px; padding: 22px 14px 0 20px; }
  .specialist__title { color: var(--navy); font-size: 13px; font-weight: 500; }
  .specialist__title span { display: block; color: var(--gold); font-size: 19px; font-weight: 500; letter-spacing: .5px; }
  .service-list { list-style: none; margin-top: 16px; }
  .service-list li { display: flex; gap: 10px; align-items: center; font-size: 11.5px; line-height: 1.15; margin-bottom: 16px; }
  .service-list svg { flex: 0 0 22px; }

  /* back */
  .capabilities { left: 0; top: 0; width: 56%; height: 170px; padding: 40px 10px 0 18px; }
  .bullets { list-style: none; font-size: 9.5px; line-height: 1.25; }
  .bullets li { position: relative; padding-left: 11px; margin-bottom: 2px; }
  .bullets li::before { content: ""; position: absolute; left: 0; top: 4px; width: 4px; height: 4px; background: var(--navy); }
  .commercial { left: 56%; top: 0; width: 44%; height: 170px; background: var(--navy);
    color: var(--white); font-size: 16px; font-weight: 300; padding: 40px 14px 0 22px; }
  .commercial::before { content: ""; position: absolute; left: -12px; top: 60px;
    border-top: 12px solid transparent; border-bottom: 12px solid transparent;
    border-right: 12px solid var(--navy); }

  .back__site { left: 0; top: 170px; width: 52%; height: 350px;
    background: linear-gradient(180deg,#a9b8c9 0%,#a98383 55%,#5d5558 100%); }
  .services { left: 52%; top: 170px; width: 48%; height: 350px; padding: 18px 12px 0 14px; }
  .services__title { color: var(--navy); font-size: 16px; font-weight: 400; margin-bottom: 10px; }
  .services .bullets { margin-bottom: 12px; }
  .services__rule { height: 2px; background: var(--navy); margin: 4px 0 12px; }

  .contact { left: 0; top: 520px; width: 60%; height: 244px; background: var(--gold);
    color: var(--white); padding: 46px 14px 0 22px; }
  .contact__title { color: var(--navy); font-size: 14px; font-weight: 500; }
  .contact__title span { display: block; color: var(--white); font-weight: 400; }
  .contact__list { list-style: none; margin-top: 18px; font-size: 11px; }
  .contact__list li { display: flex; gap: 10px; align-items: center; margin-bottom: 12px; line-height: 1.2; }
  .contact__list svg { flex: 0 0 12px; }
  .back__room { left: 60%; top: 520px; width: 40%; height: 244px;
    background: linear-gradient(170deg,#eceef0 0%,#b9bec4 55%,#62676e 100%); }
  .back__room::before { content: ""; position: absolute; left: -1px; top: 40px;
    border-top: 12px solid transparent; border-bottom: 12px solid transparent;
    border-left: 12px solid var(--gold); }
</style>
</head>
<body>

<section class="brochure brochure--front" aria-label="Brochure front">
  <div class="block front__topline"></div>
  <div class="photo front__hero" role="img" aria-label="Photo of a restored heritage city building facade"></div>
  <div class="block brand">
    <span class="brand__mark"></span>
    <span class="brand__name">Brightcoat<br>Painters</span>
  </div>

  <div class="block intro">
    <div class="block intro__grey"></div>
    <div class="block intro__gold heading">
      <span class="light">We are a</span><br>
      <span class="strong">Family-run<br>business with</span><br>
      <span class="navy">Over 40 year's</span><br>
      <span class="light">Experience</span>
    </div>
  </div>

  <div class="photo front__corridor" role="img" aria-label="Photo of a freshly painted aged care corridor"></div>
  <div class="block tagline heading">
    <p class="tagline__title">Friendly painting contractors</p>
    <p class="tagline__sub">Commercial painters in Australia</p>
  </div>

  <div class="block specialist">
    <h2 class="specialist__title heading">Specialist painting <span>contractors</span></h2>
    <ul class="service-list">
      <li><svg width="22" height="20" viewBox="0 0 22 20"><rect x="2" y="4" width="12" height="15" fill="var(--navy)"/><rect x="14" y="9" width="6" height="10" fill="var(--navy)"/><rect x="5" y="7" width="2" height="2" fill="#fff"/><rect x="9" y="7" width="2" height="2" fill="#fff"/><rect x="5" y="12" width="2" height="2" fill="#fff"/><rect x="9" y="12" width="2" height="2" fill="#fff"/></svg>Commercial &amp; industrial painting services</li>
      <li><svg width="22" height="20" viewBox="0 0 22 20"><rect x="2" y="2" width="15" height="6" rx="1" fill="var(--navy)"/><path d="M17 5h3v6h-9v3" fill="none" stroke="var(--navy)" stroke-width="1.6"/><rect x="9.5" y="14" width="3" height="5" fill="var(--navy)"/></svg>Floor preparation and coating services</li>
      <li><svg width="22" height="20" viewBox="0 0 22 20"><path d="M4 19V8l7-5 7 5v11z" fill="var(--navy)"/><rect x="9" y="12" width="4" height="7" fill="#fff"/></svg>New construction painting services</li>
    </ul>
  </div>
</section>

<section class="brochure brochure--back" aria-label="Brochure back">
  <div class="block capabilities">
    <ul class="bullets">
      <li>Pressure cleaning of building facades</li>
      <li>Painting of broad areas and trim to commercial interiors and exteriors</li>
      <li>Corrosion repairs and protective coatings for steel</li>
      <li>On-site spray painting</li>
      <li>Texture coatings</li>
      <li>After-hours and weekends available</li>
    </ul>
  </div>
  <div class="block commercial heading">Commercial<br>&amp; industrial<br>painting<br>services</div>

  <div class="photo back__site" role="img" aria-label="Photo of a warehouse exterior being repainted"></div>
  <div class="block services">
    <h3 class="services__title heading">Floor preparation and coating services</h3>
    <ul class="bullets">
      <li>Diamond grinding</li>
      <li>Shot blasting</li>
      <li>Glue and surface removal</li>
      <li>Epoxy and polyurethane coatings</li>
      <li>Anti-slip coatings</li>
      <li>Epoxy floors for warehouse and workshop</li>
    </ul>
    <div class="services__rule"></div>
    <h3 class="services__title heading">New construction painting services</h3>
    <ul class="bullets">
      <li>Painting of new buildings</li>
      <li>Internals and externals</li>
      <li>Spray painting and texture coatings</li>
    </ul>
  </div>

  <div class="block contact">
    <h3 class="contact__title heading">Contact our <span>painting professionals</span></h3>
    <ul class="contact__list">
      <li><svg width="12" height="14" viewBox="0 0 12 14"><path d="M6 0a5 5 0 0 1 5 5c0 4-5 9-5 9S1 9 1 5a5 5 0 0 1 5-5z" fill="#fff"/><circle cx="6" cy="5" r="1.8" fill="var(--gold)"/></svg>P.O. Box 412<br>Hillcrest, NSW 2000</li>
      <li><svg width="12" height="12" viewBox="0 0 12 12"><path d="M2 0h3l1 3-2 1.5a7 7 0 0 0 3.5 3.5L9 6l3 1v3a2 2 0 0 1-2 2C5 12 0 7 0 2a2 2 0 0 1 2-2z" fill="#fff"/></svg>1300 555 019</li>
      <li><svg width="12" height="12" viewBox="0 0 12 12"><circle cx="6" cy="6" r="5.3" fill="none" stroke="#fff" stroke-width="1.2"/><path d="M0.7 6h10.6M6 0.7c-3 3-3 7.6 0 10.6M6 0.7c3 3 3 7.6 0 10.6" fill="none" stroke="#fff" stroke-width="1"/></svg>www.brightcoatpainters.com.au</li>
    </ul>
  </div>
  <div class="photo back__room" role="img" aria-label="Photo of a freshly painted school classroom"></div>
</section>

</body>
</html>
```